81M business card

I need a business card for a life sciences consulting firm I started. The company name is 81M and the logo is attached. I am looking for something edgey and current but different from the blah standard business card.

Industry/Entity Type

Business

Requirements
Nice to have
• Both sides

```html
<!DOCTYPE html>
<html lang="en">
<head>
<meta charset="utf-8">
<title>81M LLC – Business Card</title>
<link rel="stylesheet" href="https://fonts.googleapis.com/css2?family=Open+Sans:wght@300;700&family=Arimo&display=swap">
<style>
  :root {
    --frame: #0b0a10;
    --frame-edge: #2a2440;
    --paper: #f4f4f6;
    --navy: #1c3f8c;
    --orange: #f7931e;
    --tagline: #8a8f99;
    --ink: #111111;
  }
  html, body {
    margin: 0;
    padding: 0;
    width: 1200px;
    height: 818px;
    overflow: hidden;
    background: var(--frame);
  }
  .card-frame {
    position: relative;
    width: 1200px;
    height: 818px;
    box-sizing: border-box;
    border: 3px solid var(--frame-edge);
    background: var(--frame);
  }
  .card {
    position: absolute;
    left: 18px;
    top: 18px;
    width: 1158px;
    height: 776px;
    border-radius: 10px;
    overflow: hidden;
    background: radial-gradient(ellipse at 40% 30%, #ffffff 0%, var(--paper) 70%, #e6e6ea 100%);
  }
  .card-shapes {
    position: absolute;
    inset: 0;
  }
  .brand-mark {
    position: absolute;
    left: 38px;
    top: 36px;
    width: 360px;
    height: 360px;
    border-radius: 50%;
    background: var(--navy);
  }
  .brand-name {
    position: absolute;
    left: 430px;
    top: 140px;
    margin: 0;
    font-family: "Open Sans", sans-serif;
    font-weight: 700;
    font-size: 212px;
    line-height: 1;
    color: var(--navy);
    letter-spacing: 4px;
    white-space: nowrap;
  }
  .brand-name .suffix {
    font-size: 52px;
    letter-spacing: 6px;
    margin-left: 14px;
  }
  .tagline {
    position: absolute;
    left: 433px;
    top: 360px;
    margin: 0;
    font-family: "Open Sans", sans-serif;
    font-weight: 300;
    font-size: 31px;
    letter-spacing: 1.5px;
    color: var(--tagline);
    white-space: nowrap;
  }
  .contact {
    position: absolute;
    left: 646px;
    top: 592px;
    margin: 0;
    font-family: "Arimo", sans-serif;
    font-size: 39px;
    line-height: 1.3;
    color: var(--ink);
    font-style: normal;
  }
</style>
</head>
<body>
  <div class="card-frame">
    <div class="card">
      <svg class="card-shapes" width="1158" height="776" viewBox="0 0 1158 776" aria-hidden="true">
        <polygon points="0,650 1158,412 1158,420 0,658" fill="#ffffff"/>
        <polygon points="0,658 1158,420 1158,446 0,684" fill="var(--navy)"/>
        <polygon points="0,684 1158,446 1158,776 0,776" fill="var(--orange)"/>
      </svg>
      <div class="brand-mark"></div>
      <h1 class="brand-name">81M<span class="suffix">LLC</span></h1>
      <p class="tagline">regulatory consulting and contract services</p>
      <address class="contact">
        48 Sample Road Suite 2<br>
        (555)-010-2468
      </address>
    </div>
  </div>
</body>
</html>
```